Wanted: A Simple yet Awesome Blog Hero Image

We need a hero image (blog graphic header) to replace our existing one: https://www.brantwellsupply.com//blog/soil-classification-foundation-and-pavement-design-starts-here
Want something to reflect what the blog article is about and is a reflection of the title.

Note: we are not in love with any of our hero graphics

Industry/Entity Type

Construction

Colors

Designer to choose colors to be used in the design.

Requirements
Must have
• Width must be 715px
• Height must not exceed 400px
• Content on graphic should be: Soil Classification: Foundation and Pavement Design Starts Here
Nice to have
• a product shown that is mentioned in the blog
Should not have
• a product with a Carraway logo

```html
<!DOCTYPE html>
<html lang="en">
<head>
<meta charset="utf-8">
<title>Soil Classification – Hero Concepts</title>
<link rel="stylesheet" href="https://fonts.googleapis.com/css2?family=Anton&family=Bebas+Neue&family=Montserrat:wght@600;700&display=swap">
<style>
  :root {
    --board: #787878;
    --label: #ffffff;
    --lime: #9dd00f;
    --white: #ffffff;
    --ink: #1c1c14;
    --pill-green: #8fbc1c;
    --soil-brown: #6b4423;
    --leaf-green: #3f8a1a;
    --panel: #f4f4f4;
    --steel-light: #e4e6e8;
    --steel-mid: #b9bcc0;
    --steel-dark: #8d9095;
    --chart-cream: #ece8de;
    --chart-ochre: #b8853a;
    --chart-umber: #5a3b20;
    --binder: #2a241e;
    --vane-red: #8e1b22;
  }
  * { margin: 0; padding: 0; box-sizing: border-box; }
  html, body { width: 1017px; height: 1200px; overflow: hidden; background: var(--board); }
  .board { position: relative; width: 1017px; height: 1200px; }

  .sample-label {
    position: absolute; left: 0; width: 1017px; text-align: center;
    font-family: "Montserrat", sans-serif; font-weight: 700; font-size: 34px;
    color: var(--label); line-height: 1;
  }
  .sample-label--one { top: 44px; }
  .sample-label--two { top: 585px; }

  .hero {
    position: absolute; left: 78px; width: 849px; height: 475px; overflow: hidden;
    box-shadow: 0 14px 18px rgba(0,0,0,0.35);
  }
  .hero--banner { top: 86px; }
  .hero--split { top: 649px; height: 474px; }

  .product { position: absolute; }
  .product--sieves { border-radius: 50% / 42%; background: radial-gradient(ellipse at 40% 40%, var(--steel-light) 0%, var(--steel-mid) 60%, var(--steel-dark) 100%); }
  .product--chart { border-radius: 3px; background: linear-gradient(90deg, var(--binder) 0%, var(--chart-cream) 6%, var(--chart-cream) 52%, #d8c7a4 60%, var(--chart-ochre) 78%, var(--chart-umber) 94%, var(--binder) 100%); }
  .product--penetrometer { border-radius: 6px; background: linear-gradient(180deg, var(--steel-light) 0%, var(--steel-mid) 55%, var(--steel-dark) 100%); }
  .product--penetrometer-upright { background: linear-gradient(90deg, var(--steel-dark) 0%, var(--steel-light) 45%, var(--steel-mid) 100%); }
  .product--vane { border-radius: 40%; background: radial-gradient(circle at 55% 55%, #e8e8e8 0%, #e8e8e8 22%, var(--vane-red) 30%, #5c1015 100%); }
  .product--fittings { border-radius: 30%; background: radial-gradient(ellipse at 50% 40%, var(--steel-light) 0%, var(--steel-mid) 60%, var(--steel-dark) 100%); }

  /* Banner concept */
  .banner-scene {
    position: absolute; inset: 0;
    background: linear-gradient(180deg, #181a14 0%, #1d2315 17%, #3a5a22 24%, #5f8f36 34%, #78a84c 50%, #6e9c44 55%, #3f2c1d 56%, #4a3424 75%, #3a281b 100%);
  }
  .banner-title {
    position: absolute; top: 6px; left: 0; width: 849px; text-align: center;
    font-family: "Bebas Neue", sans-serif; font-size: 103px; line-height: 1;
    color: var(--white); white-space: nowrap;
    transform: scaleX(0.91); transform-origin: 430px 0;
  }
  .banner-title .accent { color: var(--lime); }
  .tagline-pill {
    position: absolute; left: 83px; top: 104px; width: 684px; height: 40px;
    display: flex; border: 2px solid var(--white); border-radius: 20px; overflow: hidden;
    font-family: "Montserrat", sans-serif; font-weight: 700; font-size: 25px; color: var(--ink);
  }
  .tagline-pill span { display: flex; align-items: center; height: 100%; }
  .tagline-pill .lead { background: var(--pill-green); width: 374px; justify-content: center; border-right: 3px solid var(--ink); }
  .tagline-pill .rest { background: var(--white); flex: 1; justify-content: center; }

  /* Split concept */
  .split-text {
    position: absolute; left: 0; top: 0; width: 424px; height: 474px;
    background: linear-gradient(135deg, #ffffff 0%, var(--panel) 40%, #ececec 60%, #fafafa 100%);
  }
  .split-word {
    position: absolute; left: 0; width: 424px; text-align: center;
    font-family: "Anton", sans-serif; line-height: 1; white-space: nowrap;
  }
  .split-word--soil { top: 95px; left: -6px; font-size: 192px; color: var(--soil-brown); transform: scaleY(0.93); transform-origin: top; }
  .split-word--class { top: 281px; font-size: 56px; color: var(--leaf-green); letter-spacing: -0.5px; }
  .split-sub {
    position: absolute; left: 0; top: 337px; width: 424px; text-align: center;
    font-family: "Montserrat", sans-serif; font-weight: 700; font-size: 21.5px; line-height: 30px;
    color: var(--soil-brown);
  }
  .split-scene {
    position: absolute; left: 424px; top: 0; width: 425px; height: 474px;
    background: linear-gradient(180deg, #050805 0%, #1c3a18 15%, #2f6a28 28%, #24461e 42%, #4a3322 51%, #5a3d28 75%, #3e2a1b 100%);
  }
</style>
</head>
<body>
<main class="board">
  <p class="sample-label sample-label--one">sample- 1</p>

  <section class="hero hero--banner">
    <div class="banner-scene" role="img" aria-label="Photo of dark soil under a green sky glow"></div>
    <div class="product product--sieves" style="left:43px; top:300px; width:234px; height:118px;" role="img" aria-label="Two stainless test sieves"></div>
    <div class="product product--chart" style="left:331px; top:188px; width:251px; height:202px;" role="img" aria-label="Open soil colour chart book"></div>
    <div class="product product--penetrometer" style="left:308px; top:401px; width:263px; height:29px;" role="img" aria-label="Pocket penetrometer"></div>
    <div class="product product--vane" style="left:605px; top:372px; width:84px; height:75px;" role="img" aria-label="Red pocket vane tester"></div>
    <div class="product product--fittings" style="left:697px; top:378px; width:130px; height:64px;" role="img" aria-label="Vane tester adapter heads"></div>
    <h1 class="banner-title"><span class="accent">Soil</span> Classification</h1>
    <p class="tagline-pill"><span class="lead">Foundation &amp; Pavement</span><span class="rest">Design Starts Here</span></p>
  </section>

  <p class="sample-label sample-label--two">sample-2</p>

  <section class="hero hero--split">
    <div class="split-text">
      <h2 class="split-word split-word--soil">SOIL</h2>
      <p class="split-word split-word--class">CLASSIFICATION</p>
      <p class="split-sub">Foundation &amp; Pavement<br>Design Starts Here</p>
    </div>
    <div class="split-scene" role="img" aria-label="Photo of soil with blurred green foliage behind"></div>
    <div class="product product--chart" style="left:475px; top:132px; width:260px; height:211px;" role="img" aria-label="Open soil colour chart book"></div>
    <div class="product product--penetrometer product--penetrometer-upright" style="left:787px; top:89px; width:29px; height:242px;" role="img" aria-label="Pocket penetrometer standing upright"></div>
    <div class="product product--sieves" style="left:444px; top:366px; width:164px; height:80px;" role="img" aria-label="Two stainless test sieves"></div>
    <div class="product product--vane" style="left:634px; top:374px; width:69px; height:67px;" role="img" aria-label="Red pocket vane tester"></div>
    <div class="product product--fittings" style="left:715px; top:380px; width:112px; height:61px;" role="img" aria-label="Vane tester adapter heads"></div>
  </section>
</main>
</body>
</html>
```